A new presentation to our clients

we are a Real Estate agency, our website is www.dorelumia.com and it’s time to have a new, fashion and remarcable Business Card. we want to differentiate ourselves from other companies so we want a business card that differentiates us. we want the business card to impact our customers. in the competitive market that we have today, we have to be different and it is this difference that we seek

Target Market(s)

Real Estate Clients

Contact Information for Business Card

We search a totaly diferent card from the usual

Font styles to use
Sans Serif

Colors
e34197

Requirements
Must have
• Logo, adress, phone contact, e-mail, photo, and our website
Nice to have
• We would like to see a modern business card
Should not have
• Houses or building draws

```html
<!DOCTYPE html>
<html lang="en">
<head>
<meta charset="utf-8">
<title>Dore Lumia — Business Card</title>
<link rel="stylesheet" href="https://fonts.googleapis.com/css2?family=Barlow:wght@400;600&display=swap">
<style>
  :root {
    --backdrop: #e6e6e8;
    --card: #ffffff;
    --brand-pink: #ec2f78;
    --brand-pink-dark: #c41d5e;
    --frame-pink: #f08ab2;
    --on-pink: #ffffff;
  }
  * { margin: 0; padding: 0; box-sizing: border-box; }
  html, body {
    width: 1200px; height: 799px; overflow: hidden;
    background: var(--backdrop);
    font-family: "Barlow", sans-serif;
  }
  .business-card {
    position: absolute; left: 30px; top: 68px;
    width: 1140px; height: 662px;
    background: var(--card);
    box-shadow: 0 2px 6px rgba(0,0,0,0.18);
    overflow: hidden;
  }
  .brand-name {
    position: absolute; left: 0; right: 0; top: 78px;
    text-align: center;
    font-size: 176px; font-weight: 600; line-height: 1;
    letter-spacing: 2px;
    color: var(--brand-pink);
  }
  .footer-band { position: absolute; left: 0; top: 0; width: 1140px; height: 662px; }
  .photo-frame {
    position: absolute; left: 862px; top: 272px;
    width: 185px; height: 203px;
    background: var(--card);
    border: 2px solid var(--frame-pink);
  }
  .contact-item {
    position: absolute;
    display: flex; align-items: flex-start; gap: 12px;
    color: var(--on-pink);
    font-size: 26px; font-weight: 400; line-height: 38px;
  }
  .contact-icon {
    width: 20px; height: 20px; margin-top: 9px; flex: none;
  }
  .contact-address { left: 38px; top: 515px; }
  .contact-phone { left: 470px; top: 515px; }
  .contact-web { left: 767px; top: 511px; }
  .contact-web .line { display: flex; align-items: flex-start; gap: 12px; }
</style>
</head>
<body>
  <div class="business-card">
    <svg class="footer-band" viewBox="0 0 1140 662" aria-hidden="true">
      <path d="M10 428 L14 420 L770 420 L795 368 L1140 368 L1140 378 L800 378 L776 430 L10 430 Z" fill="var(--brand-pink-dark)"/>
      <path d="M0 437 L778 437 L803 385 L1140 385 L1140 662 L0 662 Z" fill="var(--brand-pink)"/>
    </svg>

    <h1 class="brand-name">Dore Lumia</h1>

    <div class="photo-frame" aria-label="Photo area"></div>

    <div class="contact-item contact-address">
      <svg class="contact-icon" viewBox="0 0 20 20" aria-hidden="true">
        <circle cx="10" cy="10" r="10" fill="var(--on-pink)"/>
        <path d="M10 4 a4 4 0 0 1 4 4 c0 3 -4 8 -4 8 s-4 -5 -4 -8 a4 4 0 0 1 4 -4 z" fill="var(--brand-pink)"/>
        <circle cx="10" cy="8" r="1.5" fill="var(--on-pink)"/>
      </svg>
      <div>Rua das Camélias, 418<br>4150-262, Vale Serrano</div>
    </div>

    <div class="contact-item contact-phone">
      <svg class="contact-icon" viewBox="0 0 20 20" aria-hidden="true">
        <circle cx="10" cy="10" r="10" fill="var(--on-pink)"/>
        <path d="M6.5 5 l2 -0.3 1.2 2.6 -1.3 1 c0.6 1.3 1.5 2.2 2.8 2.8 l1 -1.3 2.6 1.2 -0.3 2 c-4.5 0.4 -8.4 -3.5 -8 -8 z" fill="var(--brand-pink)"/>
      </svg>
      <div>00351 229 481 305<br>00351 229 481 306</div>
    </div>

    <div class="contact-item contact-web">
      <div>
        <div class="line">
          <svg class="contact-icon" viewBox="0 0 20 20" aria-hidden="true">
            <circle cx="10" cy="10" r="10" fill="var(--on-pink)"/>
            <rect x="5" y="6.5" width="10" height="7" rx="1" fill="var(--brand-pink)"/>
            <path d="M5.5 7 L10 10.5 L14.5 7" stroke="var(--on-pink)" stroke-width="1" fill="none"/>
          </svg>
          <span>geral@dorelumia.com</span>
        </div>
        <div class="line">
          <svg class="contact-icon" viewBox="0 0 20 20" aria-hidden="true">
            <circle cx="10" cy="10" r="10" fill="var(--on-pink)"/>
            <circle cx="10" cy="10" r="5" fill="none" stroke="var(--brand-pink)" stroke-width="1.4"/>
            <path d="M5 10 H15 M10 5 C7.5 8 7.5 12 10 15 M10 5 C12.5 8 12.5 12 10 15" stroke="var(--brand-pink)" stroke-width="1.1" fill="none"/>
          </svg>
          <span>www.dorelumia.com</span>
        </div>
      </div>
    </div>
  </div>
</body>
</html>
```